Erstellung Etikettendesign für Duschgel in Motorölflaschenoptik als Geschenkartikel für Männer
Zielgruppe
Wir sind Versandhändler aus dem Bereich Büro Basteln Schule und Geschenkartikel und verkaufen neben Handelsware aus diesem Bereich auch viele eigene selbst gestaltete Artikel unter unserem Firmennamen morvalo
Aufgabenstellung
Erstellt werden soll ein neues zusätzliches Etikettendesign für unseren Artikel Duschgel für Männer
Das Duschgel wird in Form in einer Motorölflasche geliefert und ist so ein Geschenkartikel für Männer zum Geburtstag, Weihnachten, Vatertag usw.
Die Flaschenfarbe ist immer schwarz
und der Verschluss ist rot
bzgl dem Etikettendesign sind wir für alle kreativen Ideen offen.
Es dürfen allerdings keine anderen Markenrechte verletzt werden
Unter dem Link
https://www.kaufwelt-shop.de/dp/K7R2MXQ9D3
finden sie unsere aktuellen Designs.
Bei solchen Designumsetzungen ist natürlich immer darauf zu achten nicht zu nahe an einem geschützten Produktdesign zu liegen.
Es werden hier mehrere Ideen gesammelt
Es wird bei guten Entwürfen auch mehrere Gewinner geben und mehrere Designs kommen zur Umsetzung.
Nach Auswahl zum Gewinner müssten dann noch die Druckdatei für die Etiketten und ein Produktfoto erstellt werden.
Vorlage für Druckdatei und Beispiel Produktfoto anbei
Aufgabe ist hierbei nicht das Design KL-73 anders umzusetzen sondern andere ganz neue Ideen als Etikett umzusetzen

```html
<!DOCTYPE html>
<html lang="de">
<head>
<meta charset="utf-8">
<title>TORQIN 5R Duschgel – Etikett</title>
<link rel="stylesheet" href="https://fonts.googleapis.com/css2?family=Montserrat:wght@300;500;700;800&display=swap">
<style>
  :root {
    --page: #ffffff;
    --label-black: #0b0b0b;
    --brand-red: #e3141b;
    --white: #ffffff;
    --green-bright: #7cc242;
    --green-mid: #4f9a3a;
    --green-deep: #1f4a22;
    --art-light: #eef2ea;
    --art-mid: #9aa894;
  }
  html, body {
    margin: 0;
    padding: 0;
    width: 1200px;
    height: 1198px;
    overflow: hidden;
    background: var(--page);
  }
  .label {
    position: absolute;
    left: 220px;
    top: 119px;
    width: 760px;
    height: 960px;
    display: block;
  }
  .brand-name {
    font-family: "Montserrat", sans-serif;
    font-weight: 700;
    font-size: 56px;
    fill: var(--white);
  }
  .volume {
    font-family: "Montserrat", sans-serif;
    font-weight: 700;
    font-size: 30px;
    fill: var(--white);
  }
  .series {
    font-family: "Montserrat", sans-serif;
    font-weight: 800;
    font-size: 82px;
    fill: var(--white);
  }
  .grade {
    font-family: "Montserrat", sans-serif;
    font-weight: 800;
    font-size: 62px;
    fill: var(--green-bright);
  }
  .viscosity {
    font-family: "Montserrat", sans-serif;
    font-weight: 300;
    font-size: 64px;
    fill: var(--green-bright);
  }
  .tech-line {
    font-family: "Montserrat", sans-serif;
    font-weight: 500;
    font-size: 34px;
    fill: var(--white);
  }
</style>
</head>
<body>
<svg class="label" viewBox="0 0 760 960" xmlns="http://www.w3.org/2000/svg" aria-label="Etikett TORQIN Duschgel">
  <defs>
    <linearGradient id="glow" x1="0" y1="1" x2="1" y2="0">
      <stop offset="0" stop-color="var(--green-deep)" stop-opacity="0"/>
      <stop offset="0.35" stop-color="var(--green-mid)" stop-opacity="0.9"/>
      <stop offset="0.55" stop-color="var(--green-bright)" stop-opacity="0.85"/>
      <stop offset="0.8" stop-color="var(--green-deep)" stop-opacity="0.6"/>
      <stop offset="1" stop-color="var(--green-deep)" stop-opacity="0"/>
    </linearGradient>
    <linearGradient id="art-fill" x1="0" y1="0" x2="1" y2="1">
      <stop offset="0" stop-color="var(--art-light)"/>
      <stop offset="1" stop-color="var(--art-mid)"/>
    </linearGradient>
  </defs>

  <rect class="label-base" x="0" y="0" width="760" height="960" fill="var(--label-black)"/>

  <polygon class="green-glow" points="250,720 760,330 760,760 250,960" fill="url(#glow)"/>

  <polygon class="side-band" points="0,0 325,0 250,960 0,960" fill="var(--brand-red)"/>

  <text class="brand-name" x="24" y="90">TORQIN</text>

  <text class="volume" x="20" y="940">350 ml ℮</text>

  <text class="series" x="322" y="300">5R</text>
  <text class="grade" x="322" y="372">4200</text>
  <text class="viscosity" x="320" y="444">18W240</text>
  <text class="tech-line" x="320" y="498">SCHAUM-PRO 3.0</text>

  <rect class="shower-art" x="300" y="540" width="300" height="420" fill="url(#art-fill)" role="img" aria-label="Illustration: Mann unter einer Dusche, schwarz-weiß"/>
</svg>
</body>
</html>
```